A private security company called "Tavrin Security Services Ltd"

Hello everybody,

We need a web page for a company based in NZ. It is mainly an informative website so it would be wonderful if the designer puts their absolute best into making it a website that I would really appreciate. The website needs to show professionalism and also needs to make our web surfers find the information they need in a click. the company's colour is black and silver, and if those two colours could be integrated into the website it would be absolutely lovely. Please do contact me for any information.

Sincerely,
Dorian Velasko

Industry/Entity Type

Security

```html
<!DOCTYPE html>
<html lang="en">
<head>
<meta charset="utf-8">
<title>Tavrin Security Services Ltd</title>
<link href="https://fonts.googleapis.com/css2?family=Raleway:wght@500&family=Source+Sans+3:wght@400;600&family=Libre+Caslon+Text&family=Open+Sans:wght@400&display=swap" rel="stylesheet">
<style>
:root{
  --black:#222222;
  --charcoal:#2b2b2b;
  --ink:#111111;
  --text:#333333;
  --silver-band:#ebebeb;
  --silver-line:#b5b5b5;
  --rule:#a9a9a9;
  --footer-text:#bdbdbd;
  --white:#ffffff;
}
*{margin:0;padding:0;box-sizing:border-box}
html,body{width:1151px;height:1200px;overflow:hidden;background:var(--white)}
body{position:relative;font-family:Arial,Helvetica,sans-serif;color:var(--text)}
.abs{position:absolute}

.site-header{left:0;top:0;width:1151px;height:84px;background:var(--white)}
.brand-square{left:145px;top:22px;width:38px;height:38px;background:var(--ink)}
.brand{left:96px;top:91px;z-index:2;font-family:"Source Sans 3",sans-serif;color:var(--ink)}
.brand-name{font-size:25px;font-weight:600;letter-spacing:3px;line-height:1}
.brand-sub{font-size:11px;font-weight:600;letter-spacing:.3px;margin-top:1px}
.call{left:804px;top:22px;display:flex;align-items:center;gap:12px}
.call-label{font-family:"Open Sans",sans-serif;font-size:14px;color:#444;line-height:1}
.call-number{font-family:Arial,sans-serif;font-size:25px;color:#555;letter-spacing:-.5px;line-height:1.05}

.main-nav{left:0;top:84px;width:1151px;height:47px;background:linear-gradient(#dcdcdc,#ffffff 45%,#f4f4f4)}
.main-nav ul{list-style:none;position:absolute;right:62px;top:0;height:47px;display:flex}
.main-nav li{font-family:Raleway,sans-serif;font-weight:500;font-size:15px;color:var(--ink);letter-spacing:.5px;line-height:47px;padding:0 30px;position:relative}
.main-nav li+li::before{content:"";position:absolute;left:0;top:8px;height:32px;border-left:1px solid #c9c9c9}
.main-nav li:last-child{padding-right:0}

.hero{left:0;top:131px;width:1151px;height:385px;background:var(--black)}
.hero-rule{left:0;top:516px;width:1151px;height:7px;background:var(--rule)}
.hero-photo{left:94px;top:147px;width:958px;height:343px;background:linear-gradient(180deg,#8a8a8a 0%,#5f5f5f 45%,#9a9a9a 75%,#6d6d6d 100%)}
.hero-caption{left:283px;top:305px;width:553px;height:58px;background:rgba(0,0,0,.55);color:var(--white);font-family:"Libre Caslon Text",serif;font-size:33px;line-height:58px;text-align:center}

.welcome{left:96px;top:572px;width:652px}
.welcome h1{font-family:"Source Sans 3",sans-serif;font-weight:600;font-size:23px;color:var(--ink);letter-spacing:.6px;margin-bottom:10px}
.welcome p{font-size:12px;line-height:19.2px;color:var(--text);margin-bottom:19px}

.services-box{left:785px;top:558px;width:267px;height:193px;background:var(--charcoal);padding:13px 21px}
.services-box h2{font-family:"Source Sans 3",sans-serif;font-weight:600;font-size:23px;color:var(--white);letter-spacing:.6px;margin-bottom:11px}
.services-box ul{list-style:none}
.services-box li{font-size:12px;color:var(--white);line-height:27px;padding-left:18px;position:relative}
.services-box li::before{content:"";position:absolute;left:4px;top:10px;border-left:7px solid #cfcfcf;border-top:4px solid transparent;border-bottom:4px solid transparent}

.offer{left:0;top:795px;width:1151px;height:313px;background:var(--silver-band)}
.offer-title{left:0;top:810px;width:1151px;text-align:center;font-family:"Libre Caslon Text",serif;font-weight:400;font-size:32px;line-height:44px;color:var(--ink)}
.offer-rule{top:832px;height:1px;background:var(--silver-line)}
.offer-arrow{top:826px}

.card{top:900px;width:209px;height:145px;background:var(--white);border:1px solid #c4c4c4;text-align:center}
.card-mark{position:absolute;left:50%;top:6px;width:30px;height:30px;margin-left:-15px;border-radius:50%;background:var(--ink)}
.card h3{font-family:"Source Sans 3",sans-serif;font-weight:400;font-size:22px;line-height:28px;color:var(--ink);position:absolute;left:0;right:0;top:53px}
.more{font-family:"Source Sans 3",sans-serif;font-size:12px;color:#333;white-space:nowrap}
.card .more{position:absolute;left:0;right:0;bottom:6px}
.chev{font-size:11px;letter-spacing:-2px;font-weight:600}
.more-all{right:96px;top:1080px}

.site-footer{left:0;top:1108px;width:1151px;height:92px;background:var(--charcoal)}
.footer-nav{left:105px;top:1131px;font-size:12px;color:var(--footer-text);word-spacing:2px}
.footer-nav span{margin:0 13px}
.legal{left:104px;top:1163px;font-size:11px;color:var(--footer-text)}
.footer-brand{left:952px;top:1132px;font-family:"Source Sans 3",sans-serif;color:var(--white);text-align:center}
.footer-brand .brand-name{font-size:19px;letter-spacing:2px}
.footer-brand .brand-sub{font-size:9px;margin-top:2px}
</style>
</head>
<body>
<header class="site-header abs">
  <div class="call abs">
    <svg width="28" height="28" viewBox="0 0 24 24" aria-hidden="true"><path fill="#555" d="M6.6 10.8c1.4 2.8 3.8 5.1 6.6 6.6l2.2-2.2c.3-.3.7-.4 1-.2 1.1.4 2.3.6 3.6.6.6 0 1 .4 1 1V20c0 .6-.4 1-1 1C10.6 21 3 13.4 3 4c0-.6.4-1 1-1h3.5c.6 0 1 .4 1 1 0 1.3.2 2.5.6 3.6.1.3 0 .7-.2 1z"/></svg>
    <div>
      <div class="call-label">Call Now Today</div>
      <div class="call-number">+64 (9) 555-01-42</div>
    </div>
  </div>
</header>
<div class="brand-square abs"></div>

<nav class="main-nav abs">
  <ul><li>HOME</li><li>ABOUT</li><li>SERVICES</li><li>BLOG</li><li>CONTACT US</li></ul>
</nav>
<div class="brand abs">
  <div class="brand-name">TAVRIN</div>
  <div class="brand-sub">Security Services Ltd.</div>
</div>

<section class="hero abs"></section>
<div class="hero-photo abs" role="img" aria-label="Photograph of two uniformed security guards standing at a glass building entrance"></div>
<div class="hero-caption abs">Personal bodyguard for high net</div>
<div class="hero-rule abs"></div>

<section class="welcome abs">
  <h1>Welcome to Tavrin Security Services Ltd.</h1>
  <p>Lorem ipsum dolor sit amet, consectetur adipiscing elit. Quisque dapibus accumsan orci, pretium eleifend arcu adipiscing eget. Fusce accumsan facilisis tincidunt. Phasellus tempor enim purus, vitae venenatis est. Ut imperdiet hendrerit pulvinar. Cras at tellus a enim condimentum mollis ut et tellus.</p>
  <p>Mauris dolor magna, elementum eu dictum eu, fermentum a nibh. Praesent ut dui lectus, vel lacinia sem. Praesent commodo malesuada urna, quis convallis risus dictum et. Nunc dapibus interdum libero, et semper eros auctor ac.</p>
</section>

<aside class="services-box abs">
  <h2>Our Services</h2>
  <ul>
    <li>Sed ut perspiciatis unde omnis iste</li>
    <li>Accusantium doloremque laudant</li>
    <li>Rotam rem aperiam eaque ipsa uae</li>
    <li>Aillo inventore veritatis et quasi</li>
  </ul>
</aside>

<section class="offer abs"></section>
<div class="offer-rule abs" style="left:104px;width:225px"></div>
<svg class="offer-arrow abs" style="left:334px" width="13" height="13" viewBox="0 0 14 14" aria-hidden="true"><path d="M1 0L13 7L1 14Z" fill="#8a8a8a"/></svg>
<h2 class="offer-title abs">The services i provide are:</h2>
<svg class="offer-arrow abs" style="left:808px" width="13" height="13" viewBox="0 0 14 14" aria-hidden="true"><path d="M13 0L1 7L13 14Z" fill="#8a8a8a"/></svg>
<div class="offer-rule abs" style="left:826px;width:224px"></div>

<article class="card abs" style="left:96px"><span class="card-mark"></span><h3>Property<br>Guards</h3><div class="more">More Details <span class="chev">&gt;&gt;</span></div></article>
<article class="card abs" style="left:349px"><span class="card-mark"></span><h3 style="top:50px">Corporate events<br>security</h3><div class="more">More Details <span class="chev">&gt;&gt;</span></div></article>
<article class="card abs" style="left:597px"><span class="card-mark"></span><h3>Security<br>Consultancy</h3><div class="more">More Details <span class="chev">&gt;&gt;</span></div></article>
<article class="card abs" style="left:845px"><span class="card-mark"></span><h3>Private<br>Investigation</h3><div class="more">More Details <span class="chev">&gt;&gt;</span></div></article>
<div class="more more-all abs">More Than <span class="chev">&gt;&gt;</span></div>

<footer class="site-footer abs"></footer>
<div class="footer-nav abs">HOME<span>|</span>ABOUT<span>|</span>SERVICES<span>|</span>BLOG<span>|</span>CONTACT uS</div>
<div class="legal abs">© 2014 . All right reserved. Privacy Policy | &nbsp;Terms &amp; Conditions</div>
<div class="footer-brand abs">
  <div class="brand-name">TAVRIN</div>
  <div class="brand-sub">Security Services Ltd.</div>
</div>
</body>
</html>
```